Jewelry Back Card Graphic Design

I am looking for a graphic design to print out and put in the back of the jewelry box for my long-distance jewelry. I attached an example that I am now using for the "amber comet jewelry" so you can see what it's used for.

But this card needs to relate to people who are in a long-distance relationship or friendship, so it needs to resonate with them when they see it on the website and open the box if they receive the jewelry as a gift.

I attached a rough idea that I sketched myself, but you can be creative and create anything else if you have a better idea.

It needs to be square.

Looking forward to the results!

```html
<!DOCTYPE html>
<html lang="en">
<head>
<meta charset="utf-8">
<title>A true connection goes beyond horizons</title>
<link rel="stylesheet" href="https://fonts.googleapis.com/css2?family=Herr+Von+Muellerhoff&family=Montserrat:wght@300&display=swap">
<style>
  :root {
    --night: #000000;
    --sky-deep: #1c0fa8;
    --sky-magenta: #d0124a;
    --sunset-red: #f41a0c;
    --sunset-orange: #ff8a00;
    --sunset-yellow: #ffe24a;
    --sea-red: #a80c04;
    --ink: #ffffff;
  }
  html, body {
    margin: 0;
    padding: 0;
    width: 1200px;
    height: 1200px;
    overflow: hidden;
    background: var(--night);
  }
  .card {
    position: relative;
    width: 1200px;
    height: 1200px;
    background: var(--night);
    overflow: hidden;
  }
  .sunset-scene {
    position: absolute;
    left: 0;
    top: 0;
    width: 1200px;
    height: 900px;
    background:
      radial-gradient(ellipse 520px 260px at 620px 520px,
        rgba(255, 226, 74, 0.95) 0,
        rgba(255, 138, 0, 0.6) 55%,
        rgba(255, 138, 0, 0) 100%),
      linear-gradient(to bottom,
        var(--sky-deep) 0,
        var(--sky-magenta) 150px,
        var(--sunset-red) 290px,
        var(--sunset-orange) 440px,
        var(--sunset-red) 640px,
        var(--sea-red) 700px,
        #4a0402 800px,
        var(--night) 900px);
  }
  .tagline {
    position: absolute;
    left: 0;
    width: 1200px;
    margin: 0;
    text-align: center;
    color: var(--ink);
    white-space: nowrap;
  }
  .tagline-script {
    top: 862px;
    font-family: "Herr Von Muellerhoff", cursive;
    font-weight: 400;
    font-size: 190px;
    line-height: 1;
    padding-left: 16px;
  }
  .tagline-caps {
    top: 1034px;
    font-family: "Montserrat", sans-serif;
    font-weight: 300;
    font-size: 66px;
    line-height: 1;
    letter-spacing: 1px;
    padding-left: 16px;
  }
</style>
</head>
<body>
  <main class="card">
    <div class="sunset-scene" role="img" aria-label="Illustration of a tropical sunset over the sea, framed by silhouetted palm leaves"></div>
    <p class="tagline tagline-script">A true connection</p>
    <p class="tagline tagline-caps">GOES BEYOND HORIZONS</p>
  </main>
</body>
</html>
```